Tolva Cafe Coffee Beans Bag Design

We are an Ethiopian owned coffee shop in D.C looking to create an eye catching design to put onto bag of beans to sell. Our brand is surrounding innovating and modernizing Ethiopian coffee with a chic retro theme. Our bags should highlight the origin of the beans, sustainability as well as general info about the specific beans or at least a space for it. Uploaded is our current logo and we would love if the colors incorporated on the bag play well with our brand color, that beautiful emerald/blue-green. I have also uploaded some other coffee brands coffee bags as inspiration for the direction we would like to go with regarding the design and bag type. Lastly, I have also uploaded the template that the bag manufacturers have asked us to design the bags with these dimensions in mind, so designing the bags within the bounds of this bag would be required. Thank you!

Target Market(s)

Coffee market

Industry/Entity Type

Coffee/Cafe & Restaurant Merchandize

Font styles to use
Other font styles liked:
• Rockwell, Bodoni, Gabriela Stencil

Colors
0054AA
0677BA
7BADD7
CADEEF
E8F1F8
0094D4
00A9DD
6FCCEA
C7EBF8
E9F6FB
00AB8E
00BBA5
67D7C9
C6EFE9
E9F9F6

Requirements
Must have
• Must incorporate a logo and include a space to include information about the beans
Nice to have
• A 70s vintage/funky design feeling to the bag. We would love if the bag design felt novel or interesting to catch customers attention and for the design to not be one that blends in with other coffee bags. This is something that should stand out and be fun.
Should not have
• The bag design shouldn't be a cut and dry design. Whether in the form of a simple sticker or slapping the logo onto the bag itself, the design should be novel and shouldn't look straight forward and boring.

```html
<!DOCTYPE html>
<html lang="en">
<head>
<meta charset="utf-8">
<title>Tolva Cafe – Coffee Bag Front</title>
<link rel="stylesheet" href="https://fonts.googleapis.com/css2?family=Bodoni+Moda:wght@500&family=Montserrat:wght@500;600;700&display=swap">
<style>
  :root {
    --page: #ffffff;
    --mint: #c9e9e4;
    --mint-light: #e9f6f3;
    --emerald: #0fa580;
    --ink: #133a2c;
    --navy: #1b3f86;
    --blue: #1f56b3;
    --pink: #f1b9d8;
  }
  * { margin: 0; padding: 0; box-sizing: border-box; }
  html, body {
    width: 1200px;
    height: 1200px;
    overflow: hidden;
    background: var(--page);
  }
  .bag-front {
    position: absolute;
    left: 100px;
    top: 133px;
    width: 1000px;
    height: 933px;
    display: flex;
    gap: 7px;
  }
  .pattern-panel {
    width: 289px;
    height: 100%;
    background: linear-gradient(90deg,
      var(--navy) 0%, var(--emerald) 12%, var(--blue) 24%, var(--emerald) 36%,
      var(--pink) 48%, var(--emerald) 60%, var(--navy) 72%, var(--emerald) 84%, var(--blue) 100%);
  }
  .label-panel {
    flex: 1;
    height: 100%;
    background: var(--mint);
    position: relative;
    text-align: center;
  }
  .brand-name {
    position: absolute;
    top: 200px;
    left: 0;
    right: 0;
    font-family: "Bodoni Moda", serif;
    font-weight: 500;
    font-size: 92px;
    line-height: 0.95;
    color: var(--emerald);
  }
  .product-title {
    position: absolute;
    top: 428px;
    left: 0;
    right: 0;
    font-family: "Montserrat", sans-serif;
    font-weight: 600;
    font-size: 34px;
    letter-spacing: 0.3em;
    padding-left: 0.3em;
    color: var(--ink);
  }
  .roast-level {
    position: absolute;
    top: 484px;
    left: 0;
    right: 0;
    font-family: "Montserrat", sans-serif;
    font-weight: 500;
    font-size: 17px;
    letter-spacing: 0.04em;
    color: var(--ink);
  }
  .bean-info-box {
    position: absolute;
    top: 564px;
    left: 12px;
    right: 12px;
    height: 252px;
    background: var(--mint-light);
  }
  .origin-line {
    position: absolute;
    top: 864px;
    left: 0;
    right: 0;
    font-family: "Montserrat", sans-serif;
    font-weight: 700;
    font-size: 13px;
    letter-spacing: 0.04em;
    color: var(--ink);
  }
</style>
</head>
<body>
  <main class="bag-front">
    <div class="pattern-panel" role="img" aria-label="Retro wavy vertical vine pattern in navy, blue, emerald and pink"></div>
    <section class="label-panel">
      <h1 class="brand-name">Tolva<br>Cafe</h1>
      <p class="product-title">COFFEE</p>
      <p class="roast-level">MEDIUM ROAST</p>
      <div class="bean-info-box" aria-label="Space for bean information"></div>
      <p class="origin-line">ROASTED IN WASHINGTON, DC</p>
    </section>
    <div class="pattern-panel" role="img" aria-label="Retro wavy vertical vine pattern in navy, blue, emerald and pink"></div>
  </main>
</body>
</html>
```